bRm Design Group - architect web site

need a web site to permit potential clients to view our portfolio of work.

Will need lots of photos included.

Industry/Entity Type

Architect

Coding

Coded - Design and coding required

Number of Pages Required

5+ page

Font styles to use
Sans Serif

Requirements
Must have
• photos should be organized by project - perhaps a summary of photos and then click to enlarge? should be simple to operate. should be able to separate interior design from architecture.
• needs to be easy to add more photos in the future.

```html
<!DOCTYPE html>
<html lang="en">
<head>
<meta charset="utf-8">
<title>bRm Design Group</title>
<link href="https://fonts.googleapis.com/css2?family=Noto+Sans:wght@400;700&family=Noto+Serif:ital,wght@1,700&display=swap" rel="stylesheet">
<style>
:root{
  --band:#86848a;
  --stage:#e8e8e8;
  --white:#ffffff;
  --ink:#3a3a3a;
  --muted:#8a8a8a;
  --icon:#555555;
  --client:#6a6a6a;
}
*{margin:0;padding:0;box-sizing:border-box}
html,body{width:1200px;height:807px;overflow:hidden}
body{position:relative;background:var(--white);font-family:"Noto Sans",sans-serif;color:var(--ink)}

.site-header{position:absolute;left:0;top:0;width:1200px;height:115px;background:var(--band)}
.brand{position:absolute;left:112px;top:42px;display:flex;align-items:center;gap:10px;color:var(--white);font-size:22px;font-weight:700;letter-spacing:.3px;white-space:nowrap}
.brand-mark{width:18px;height:18px;background:var(--white)}
.main-nav{position:absolute;top:50px;left:606px;width:450px;height:22px}
.main-nav a{position:absolute;top:0;color:var(--white);text-decoration:none;font-size:15px;white-space:nowrap}

.stage{position:absolute;left:0;top:115px;width:1200px;height:487px;background:var(--stage)}
.slide{position:absolute;background:var(--white);box-shadow:0 1px 4px rgba(0,0,0,.18);overflow:hidden}
.slide-photo{position:absolute}
.slide-caption{position:absolute;font-family:"Noto Serif",serif;font-style:italic;font-weight:700;color:var(--ink);white-space:nowrap;border-left:1px solid #bbb;padding-left:14px}
.slide-caption span{font-family:"Noto Sans",sans-serif;font-weight:400;color:var(--muted)}

.slide--side{top:61px;height:320px}
.slide--side .slide-photo{top:8px;height:266px}
.slide--side .slide-caption{top:286px;font-size:10px;line-height:14px}
.slide--left{left:98px;width:400px}
.slide--left .slide-photo{left:9px;right:0;background:linear-gradient(135deg,#c9cfcf,#9aa7a0)}
.slide--left .slide-caption{left:20px}
.slide--right{left:560px;width:541px}
.slide--right .slide-photo{left:0;right:9px;background:linear-gradient(135deg,#e4e2dc,#a89e90)}
.slide--right .slide-caption{right:176px}

.slide--center{left:284px;top:22px;width:632px;height:397px}
.slide--center .slide-photo{left:11px;top:10px;width:610px;height:328px;background:linear-gradient(160deg,#ecebe8,#c4c0b6 60%,#7f9470)}
.slide--center .slide-caption{left:26px;top:354px;font-size:13px;line-height:18px}

.pager{position:absolute;top:446px;left:567px;display:flex;gap:8px}
.pager i{display:block;width:11px;height:11px;border:1px solid #8a8a8a;border-radius:50%}

.clients{position:absolute;left:112px;top:620px;width:975px;height:44px;display:flex;justify-content:space-between;align-items:center;color:var(--client);font-size:15px;font-weight:700;white-space:nowrap}

.site-footer{position:absolute;left:0;top:723px;width:1200px;height:84px;background:var(--band)}
.contact-bar{position:absolute;left:98px;top:680px;width:1003px;height:80px;background:var(--stage);font-size:13px;color:var(--ink)}
.contact-item{position:absolute;display:flex;align-items:flex-start;line-height:16px;white-space:nowrap}
.contact-item svg{flex:none;fill:var(--icon);margin-top:1px}
.social{position:absolute;right:31px;top:34px;display:flex;gap:12px;font-size:11px;font-weight:700;color:var(--icon);white-space:nowrap}
.copyright{position:absolute;left:0;top:777px;width:1200px;text-align:center;color:var(--white);font-size:12.5px}
</style>
</head>
<body>
<header class="site-header">
  <div class="brand"><span class="brand-mark"></span>bRm Design Group</div>
  <nav class="main-nav">
    <a href="#" style="left:0">Home</a>
    <a href="#" style="left:77px">About</a>
    <a href="#" style="left:155px">Portfolio</a>
    <a href="#" style="left:251px">Testimonials</a>
    <a href="#" style="left:374px">Contact</a>
  </nav>
</header>

<section class="stage">
  <figure class="slide slide--side slide--left">
    <div class="slide-photo" role="img" aria-label="Living room with white sofas and glass walls facing the sea"></div>
    <figcaption class="slide-caption">This is a slick, clean little skin. You know you want it! <span>(1 of 5)</span></figcaption>
  </figure>
  <figure class="slide slide--side slide--right">
    <div class="slide-photo" role="img" aria-label="White kitchen with glass-front cabinets and a breakfast counter"></div>
    <figcaption class="slide-caption">This is a slick, clean little skin. You know you want it! <span>(3 of 5)</span></figcaption>
  </figure>
  <figure class="slide slide--center">
    <div class="slide-photo" role="img" aria-label="Long wooden dining table under a glass chandelier, open to a garden"></div>
    <figcaption class="slide-caption">This is a slick, clean little skin. You know you want it! <span>(2 of 5)</span></figcaption>
  </figure>
  <div class="pager"><i></i><i></i><i></i><i></i></div>
</section>

<div class="clients">
  <span>Tallow</span><span>ventura</span><span>Hartwell</span><span>Brookmere</span><span>Larkfield Ltd</span><span>Orla</span><span>corvel</span><span>Quill Partners</span><span>marlowe</span><span>truepane</span>
</div>

<footer class="site-footer"></footer>

<div class="contact-bar">
  <div class="contact-item" style="left:34px;top:22px">
    <svg width="12" height="14" viewBox="0 0 12 14" style="margin-right:14px"><path d="M6 0a5 5 0 0 0-5 5c0 4 5 9 5 9s5-5 5-9a5 5 0 0 0-5-5zm0 7a2 2 0 1 1 0-4 2 2 0 0 1 0 4z"/></svg>
    <span>48, Harbour Lane<br>Portvale, City</span>
  </div>
  <div class="contact-item" style="left:304px;top:22px">
    <svg width="12" height="12" viewBox="0 0 12 12" style="margin-right:8px"><path d="M2 0l2.5 2.5-1.3 1.8a8 8 0 0 0 4.5 4.5l1.8-1.3L12 10l-2 2C4 12 0 8 0 2z"/></svg>
    <span>+60 412 7780</span>
  </div>
  <div class="contact-item" style="left:304px;top:48px">
    <svg width="13" height="13" viewBox="0 0 13 13" style="margin-right:7px"><path d="M0 3h3v10H0zM4 0h7v4h2v9H4zm2 2v2h3V2zm0 4v2h5V6zm0 3v2h5V9z"/></svg>
    <span>+60 38 215 46</span>
  </div>
  <div class="contact-item" style="left:548px;top:22px">
    <svg width="14" height="11" viewBox="0 0 14 11" style="margin-right:13px;margin-top:2px"><path d="M0 0h14v2L7 6 0 2zm0 3.5l7 4 7-4V11H0z"/></svg>
    <span>hello@brmstudio.com</span>
  </div>
  <div class="contact-item" style="left:548px;top:48px">
    <svg width="13" height="13" viewBox="0 0 13 13" style="margin-right:14px"><circle cx="6.5" cy="6.5" r="6.5"/><path d="M1.5 6.5h10M6.5 1.5c-2.5 3-2.5 7 0 10M6.5 1.5c2.5 3 2.5 7 0 10" stroke="#e8e8e8" stroke-width="1" fill="none"/></svg>
    <span>www.brmstudio.com</span>
  </div>
  <div class="social"><span>Folio</span><span>Chirp</span><span>Plus</span><span>Feed</span><span>Snap</span></div>
</div>

<p class="copyright">© 2015. www. brmdesigngroup.com. All rights reserved.</p>
</body>
</html>
```